Event for Hair Salon Wigs

We are introducing a new division of our hair salon selling hair wigs. We are introducing our clients to our wig line, which are beautiful well crafted wig. These wigs are not like granny's wigs, but wigs for women who want style and are willing to pay extra for beautiful believeable wigs. The event is casual were clients and there friends will be flowing in and out during a sunday afternoon.
The postcard should reflect a nice sunny spring day, but classy not extremely colorful. If you think a photo would add to a better look to the card....let me know and I will upload some.
Thank you
Updates

I have images that was uploaded, but have not been posted to this project. I'm not sure what's going on, but please look out for them. I have been trying to communicate with customer service, but no  response thus far. The cards I have received this far I think have to much of a colored pattern, I would love it if the logo "K Radiant Wigs" took center stage, rather than the word open house. Open House is important, but I don't won't it to be bolder than "wigs." Please leave room for address labels, and if possible, the description of the event should be in little bigger text. Oh, I am open to an abstract lady rather than the images that are uploaded, but if images are used, you don't have to use them all. Believe it or not...I do like simplicity:)                             

Industry/Entity Type

Hair

```html
<!DOCTYPE html>
<html lang="en">
<head>
<meta charset="utf-8">
<title>K Radiant Wigs – Open House Postcard</title>
<link rel="stylesheet" href="https://fonts.googleapis.com/css2?family=Questrial&display=swap">
<style>
  :root {
    --backdrop: #a3a3a3;
    --blush: #f6c9cf;
    --rose: #e79aa6;
    --rose-deep: #c9707f;
    --mauve: #8a5a78;
    --plum: #3f2a4e;
    --plum-deep: #2f2140;
    --brand-red: #d8262f;
    --paper: #ffffff;
    --ink-light: #ffffff;
    --line: #222222;
    --photo-light: #e9e4e4;
    --photo-dark: #4a332b;
  }
  * { box-sizing: border-box; margin: 0; padding: 0; }
  html, body { width: 1200px; height: 771px; overflow: hidden; }
  body {
    background: var(--backdrop);
    font-family: "Questrial", "Century Gothic", sans-serif;
    position: relative;
  }
  .postcard {
    position: absolute;
    top: 205px;
    width: 540px;
    height: 360px;
    overflow: hidden;
    box-shadow: 0 6px 18px rgba(0,0,0,.25);
  }
  .postcard--front {
    left: 50px;
    background: linear-gradient(180deg, var(--blush) 0%, var(--rose) 38%, var(--mauve) 68%, var(--plum) 86%, var(--plum-deep) 100%);
  }
  .postcard--back {
    left: 610px;
    background: linear-gradient(180deg, var(--blush) 0%, var(--rose-deep) 22%, var(--mauve) 48%, var(--plum) 75%, var(--plum-deep) 100%);
  }

  /* Front */
  .front-band {
    position: absolute; left: 0; right: 0; top: 120px; height: 92px;
    background: rgba(255,255,255,.28);
  }
  .label-frame { position: absolute; left: 145px; top: 96px; width: 250px; height: 112px; }
  .brand-name {
    color: var(--brand-red);
    font-weight: 400;
    white-space: nowrap;
  }
  .label-frame .brand-name {
    position: absolute; left: 0; right: 0; top: 40px;
    text-align: center; font-size: 28px;
  }
  .event-title {
    position: absolute; left: 0; right: 0; top: 238px;
    text-align: center; color: var(--ink-light);
    font-size: 31px; font-weight: 400; letter-spacing: 2px;
  }
  .event-date {
    position: absolute; left: 0; right: 0; top: 276px;
    text-align: center; color: var(--ink-light);
    font-size: 18px; line-height: 20px; letter-spacing: 1px;
  }

  /* Back */
  .postcard--back .brand-name {
    position: absolute; left: 20px; top: 18px; font-size: 26px;
  }
  .invite-text {
    position: absolute; left: 20px; top: 62px; width: 262px;
    color: var(--ink-light); font-size: 9.4px; line-height: 12.4px;
    text-shadow: 0 0 2px rgba(47,33,64,.55);
  }
  .invite-text p + p { margin-top: 4px; }
  .invite-text .extras { font-size: 7.5px; margin-top: 4px; }
  .wig-photo {
    position: absolute; left: 356px; top: 22px; width: 92px; height: 80px;
    background: linear-gradient(180deg, var(--photo-light) 0%, var(--photo-dark) 55%, var(--photo-light) 100%);
  }
  .stamp-panel { position: absolute; left: 455px; top: 14px; width: 85px; height: 110px; background: var(--paper); }
  .address-panel { position: absolute; left: 290px; top: 108px; width: 250px; height: 178px; background: var(--paper); }
  .stamp-box {
    position: absolute; left: 471px; top: 28px; width: 56px; height: 58px;
    border: 2px solid var(--line);
  }
  .address-line {
    position: absolute; left: 305px; width: 222px;
    border-top: 1.5px dotted var(--line);
  }
  .address-line--1 { top: 140px; }
  .address-line--2 { top: 170px; }
  .address-line--3 { top: 200px; }
  .address-line--4 { top: 230px; }
  .address-line--5 { top: 260px; }
  .contact {
    position: absolute; right: 12px; top: 293px;
    text-align: right; color: var(--ink-light); font-style: normal;
    font-size: 8.5px; line-height: 11px;
  }
</style>
</head>
<body>

<section class="postcard postcard--front" aria-label="Postcard front">
  <div class="front-band"></div>
  <div class="label-frame">
    <svg width="250" height="112" viewBox="0 0 250 112" aria-hidden="true">
      <path d="M30 8 H220 Q228 22 244 24 Q236 56 244 88 Q228 90 220 104 H30 Q22 90 6 88 Q14 56 6 24 Q22 22 30 8 Z"
            fill="#fbe7ea" stroke="#f3d3d8" stroke-width="2"/>
    </svg>
    <div class="brand-name">K Radiant Wigs</div>
  </div>
  <h1 class="event-title">OPEN HOUSE</h1>
  <p class="event-date">Sunday April 13th<br>2014 11am to 3pm</p>
</section>

<section class="postcard postcard--back" aria-label="Postcard back">
  <div class="brand-name">K Radiant Wigs</div>
  <div class="invite-text">
    <p>Hello,<br>I would like to cordially invite you to Studio Marlowe to introduce you to K Radiant Wigs, a showroom of some of the finest human and synthetic hair wigs available. Come look, feel and try on these beautiful wigs. K Radiant Wigs will be offering 15% off as an introductory offer the day of the event.</p>
    <p>If you bring a friend and a gently worn wig for charity, you will receive 15% off of the total purchase. Additionally, bring a friend and receive 20% off of the total purchase. Come join us... you might find a radiant new look for spring!</p>
    <p>Hope to see you,<br>Renee Hollis</p>
    <p class="extras">Light appetizers and Drinks<br>Raffles</p>
  </div>
  <div class="wig-photo" role="img" aria-label="Photo of a long dark brown wig on a mannequin"></div>
  <div class="stamp-panel"></div>
  <div class="address-panel"></div>
  <div class="stamp-box"></div>
  <div class="address-line address-line--1"></div>
  <div class="address-line address-line--2"></div>
  <div class="address-line address-line--3"></div>
  <div class="address-line address-line--4"></div>
  <div class="address-line address-line--5"></div>
  <address class="contact">
    www.kradiantwigs.com<br>
    555 014.2287<br>
    4810 Meadow Ln, Ste B<br>
    Fairview, Ca 90000
  </address>
</section>

</body>
</html>
```